Security Consulting Firm needs brochure to be used for advertisement and sales

Need a brochure design for a new security consulting firm based in Metro Detroit called "K. Darnell Safety Advisors, LLC" We provide consulting services related to safety and security for our clients. I have attached a file that contains excerpts from our business summary for info to be used (does not have to be word for work or exact), business contact info as well as statistics that i would like added somewhere. I also attached the company logo for use. I would like the logos for Chatterly, WorkWeave and Snapmora somewhere on the brochure as well. Lastly , I would like the final design to communicate strength, safety, investigation and protection. Thank you
Target Market(s)
Corporate, schools, places of worship, large events, VIP
Industry/Entity Type
Business Consultant
Font styles to use
Colors
Designer to choose colors to be used in the design.
Look and feel

```html
<!DOCTYPE html>
<html lang="en">
<head>
<meta charset="utf-8">
<title>K. Darnell Safety Advisors – Brochure Spread</title>
<link rel="stylesheet" href="https://fonts.googleapis.com/css2?family=Questrial&family=Didact+Gothic&display=swap">
<style>
  :root {
    --sky-deep: #1763b8;
    --sky-mid: #2b86d4;
    --sky-light: #74b8ec;
    --steel-shadow: #3d5f86;
    --steel-light: #9fbfdc;
    --ink-black: #000000;
    --paper: #ffffff;
    --accent-cyan: #4fc3e8;
    --body-text: #f2f2f2;
    --list-text: #2a2a2a;
    --headline-veil: rgba(235, 240, 250, 0.6);
    --bullet-dark: #0a6fb0;
    --bullet-light: #5fd0f2;
  }
  * { box-sizing: border-box; margin: 0; padding: 0; }
  html, body { width: 1200px; height: 850px; overflow: hidden; background: var(--paper); }
  .spread {
    position: relative;
    width: 1200px;
    height: 850px;
    overflow: hidden;
    font-family: "Didact Gothic", "Questrial", sans-serif;
  }
  .hero-photo {
    position: absolute;
    inset: 0;
    background:
      linear-gradient(62deg,
        rgba(61, 95, 134, 0) 0%,
        rgba(61, 95, 134, 0) 8%,
        rgba(61, 95, 134, 0.75) 16%,
        rgba(159, 191, 220, 0.55) 26%,
        rgba(61, 95, 134, 0) 36%),
      radial-gradient(ellipse at 68% 12%, rgba(255, 255, 255, 0.16) 0%, rgba(255, 255, 255, 0) 40%),
      linear-gradient(200deg, var(--sky-deep) 0%, var(--sky-mid) 55%, var(--sky-light) 100%);
  }
  .headline {
    position: absolute;
    inset: 0;
    font-family: "Questrial", sans-serif;
    font-weight: 400;
    color: var(--headline-veil);
    line-height: 1;
    pointer-events: none;
  }
  .headline-main {
    position: absolute;
    left: 72px;
    top: 406px;
    font-size: 131px;
    letter-spacing: -3px;
    white-space: nowrap;
  }
  .headline-sub {
    position: absolute;
    left: 336px;
    top: 518px;
    font-size: 46px;
    letter-spacing: -0.8px;
    white-space: nowrap;
  }
  .about-panel {
    position: absolute;
    left: 0;
    top: 566px;
    width: 651px;
    height: 254px;
    background: var(--ink-black);
    padding: 32px 62px 0 126px;
  }
  .about-text {
    color: var(--body-text);
    font-size: 14.6px;
    line-height: 17.9px;
  }
  .about-lead { color: var(--accent-cyan); }
  .services-panel {
    position: absolute;
    left: 651px;
    top: 566px;
    width: 549px;
    height: 254px;
    background: var(--paper);
    padding: 35px 0 0 61px;
  }
  .services-list {
    list-style: none;
    color: var(--list-text);
    font-size: 18px;
    line-height: 21.5px;
    letter-spacing: 0.2px;
  }
  .services-list li {
    position: relative;
    padding-left: 24px;
  }
  .services-list li::before {
    content: "";
    position: absolute;
    left: 2px;
    top: 6px;
    width: 9px;
    height: 9px;
    transform: rotate(45deg);
    background: linear-gradient(135deg, var(--bullet-light) 0%, var(--bullet-dark) 100%);
  }
</style>
</head>
<body>
  <main class="spread">
    <div class="hero-photo" role="img" aria-label="Photo placeholder: low-angle view of a steel power transmission pylon with glowing insulators and cables against a clear blue sky"></div>

    <h1 class="headline">
      <span class="headline-main">Over 100 years</span>
      <span class="headline-sub">of specialized worldwide security</span>
    </h1>

    <section class="about-panel">
      <p class="about-text"><span class="about-lead">We’re committed to a team-orientated client approach,</span> while striving to develop and maintain a lasting partnership through exceeding business goals and expectations. K. Darnell Safety Advisors are steadfast in our pursuit of client asset protection, which will not only mitigate risk, but maximize business performance. Lastly, K. Darnell Safety Advisors, LLC will continue to provide support and review long after initial assessments are completed to client satisfaction. K. Darnell Safety Advisors, LLC is committed to the protection of individual and corporate assets, while striving to provide client satisfaction that is not only required, but deserved.</p>
    </section>

    <section class="services-panel">
      <ul class="services-list">
        <li>Corporate Businesses</li>
        <li>Sporting/Special Event Venues</li>
        <li>Education (Public &amp; Private K-12 Schools,<br>Colleges, and University Campuses)</li>
        <li>Religious Facilities of All FaithsTravel</li>
        <li>AgenciesTransportation AgenciesPersonal</li>
        <li>Protection of High-Risk/High Profile Individuals</li>
        <li>Architectural Design</li>
      </ul>
    </section>
  </main>
</body>
</html>
```